Bref créative
Stationary and Business Cards Orla Ridge Capital
Stationary, Envelopes, Business Cards
Professional
Marcus Bellwin
Managing Partner
8734 Fernhollow Ave. Suite 4580
Los Angeles, CA 90217
marcus@orlaridgecapital.example
orlaridgecapital.example
Design should be similar to the informational side of the business card (with bull silhouette) I had designed previously (uploaded), but with colors matching my website colors of black+white+blue (see previous contest and also uploaded).
Should contain the following:
-Company Logo (uploaded)
-The Slogan "Hedge Fund Strategies at Mutual Fund Prices"
-And the offer "Free Financial Check-Up"
Here is the previous business card. I don't care about the pattern in the background as that didn't show up in printing anyway.
here is a draft version of the website, to give you an idea of the general appearance
here is the company logo

```html
<!DOCTYPE html>
<html lang="en">
<head>
<meta charset="utf-8">
<title>Orla Ridge Capital – Business Cards</title>
<link rel="stylesheet" href="https://fonts.googleapis.com/css2?family=Arimo:wght@400;700&display=swap">
<style>
  :root {
    --backdrop: #e9e7e4;
    --card-white: #ffffff;
    --band-grey: #6b6b6b;
    --band-grey-dark: #4e4e4e;
    --mark-blue: #2f7fa8;
    --edge-blue: #5aa6cf;
    --ink: #111111;
    --muted: #8a8a8a;
    --dark-top: #4a4848;
    --dark-bottom: #2c2b2b;
    --dark-text: #c9c9c9;
    --light-text: #ffffff;
    --silhouette-light: #d9d9d9;
    --silhouette-dark: #5e5c5c;
  }
  html, body {
    margin: 0;
    padding: 0;
    width: 1200px;
    height: 751px;
    overflow: hidden;
    background: var(--backdrop);
    font-family: "Arimo", Arial, sans-serif;
  }
  .canvas { position: relative; width: 1200px; height: 751px; }

  .card {
    position: absolute;
    width: 492px;
    height: 283px;
    border-radius: 18px;
    overflow: hidden;
    box-shadow: 0 6px 18px rgba(0,0,0,0.18);
  }

  /* Front */
  .card-front { left: 175px; top: 72px; background: var(--card-white); }
  .front-band {
    position: absolute; left: 41px; top: 0; width: 67px; height: 100%;
    background: linear-gradient(90deg, var(--band-grey-dark), var(--band-grey), var(--band-grey-dark));
  }
  .front-edge {
    position: absolute; right: 0; top: 0; width: 18px; height: 100%;
    background: var(--edge-blue);
  }
  .brand {
    position: absolute; left: 41px; top: 43px;
    display: flex; align-items: center; gap: 12px;
  }
  .brand-mark {
    width: 67px; height: 72px; background: var(--mark-blue);
  }
  .brand-name {
    font-weight: 700; font-size: 22px;
    color: var(--ink);
  }
  .front-silhouette {
    position: absolute; left: 209px; top: 150px; width: 180px; height: 100px;
    background: radial-gradient(ellipse at center, var(--silhouette-light), rgba(217,217,217,0) 70%);
  }
  .person {
    position: absolute; left: 108px; right: 18px; top: 132px;
    text-align: center; color: var(--ink);
  }
  .person-name { font-weight: 700; font-size: 26px; margin: 0; }
  .person-title { font-weight: 700; font-size: 13px; margin: 2px 0 0; }
  .front-url {
    position: absolute; right: 60px; top: 247px;
    font-size: 12px; color: var(--muted);
  }

  /* Back */
  .card-back {
    left: 480px; top: 400px;
    background: linear-gradient(180deg, var(--dark-top), var(--dark-bottom));
  }
  .slogan {
    position: absolute; left: 0; right: 0; top: 34px; margin: 0;
    text-align: center; color: var(--light-text);
    font-weight: 400; font-size: 18px;
  }
  .slogan-rule {
    position: absolute; left: 30px; right: 30px; top: 66px; height: 1px;
    background: linear-gradient(90deg, rgba(255,255,255,0), rgba(255,255,255,0.45), rgba(255,255,255,0));
  }
  .contact {
    position: absolute; left: 41px; top: 104px; margin: 0;
    font-style: normal; font-size: 12.5px; line-height: 17px;
    color: var(--dark-text);
  }
  .back-silhouette {
    position: absolute; left: 240px; top: 68px; width: 228px; height: 120px;
    background: radial-gradient(ellipse at center, var(--silhouette-dark), rgba(94,92,92,0) 70%);
  }
  .back-url {
    position: absolute; right: 30px; top: 192px;
    font-size: 12px; color: var(--dark-text);
  }
  .offer {
    position: absolute; left: 0; right: 0; top: 226px; height: 32px;
    display: flex; align-items: center; justify-content: center;
    background: linear-gradient(90deg, rgba(0,0,0,0), rgba(20,20,20,0.55), rgba(0,0,0,0));
    color: var(--light-text); font-size: 17px;
  }
</style>
</head>
<body>
<main class="canvas">
  <section class="card card-front" aria-label="Business card front">
    <div class="front-band"></div>
    <div class="front-edge"></div>
    <div class="brand">
      <span class="brand-mark"></span>
      <span class="brand-name">Orla Ridge Capital</span>
    </div>
    <div class="front-silhouette" role="img" aria-label="Faint bull silhouette"></div>
    <div class="person">
      <p class="person-name">Marcus Bellwin</p>
      <p class="person-title">Managing Partner</p>
    </div>
    <span class="front-url">www.orlaridgecapital.example</span>
  </section>

  <section class="card card-back" aria-label="Business card back">
    <h1 class="slogan">Hedge Fund Strategies at Mutual Fund Prices</h1>
    <div class="slogan-rule"></div>
    <div class="back-silhouette" role="img" aria-label="Faint bull silhouette"></div>
    <address class="contact">
      8734 Fernhollow Ave. Suite 4580<br>
      Los Angeles, CA 90217<br>
      Phone : 555-014-2286<br>
      Fax : 555-014-7731<br>
      Email : marcus@orlaridgecapital.example
    </address>
    <span class="back-url">www.orlaridgecapital.example</span>
    <div class="offer">Free Financial Check-Up</div>
  </section>
</main>
</body>
</html>
```